A4 Client Referral Program Flyer for Property Management Agency

Harbourleaf Estates Agency is a property management specialist based on Sydney's Northern Beaches in Australia.

We manage mid to high-end rental properties for investors and property owners.
We are currently looking to build our portfolio and are offering existing clients and contacts a referral incentive. We want to sign up more properties to manage.

We are offering the referrer a $250 referral fee and the new owner 2 months of free management to entice them to use Harbourleaf Estates Agency.

We want an A4 Flyer to print and add to other document packages we hand out to clients and suppliers.
If at all possible a matching digital banner would be great too! 1000px wide x 250px

Please find copy attached in Word Doc and our logo attached also.

Please see our website for any more details on our business.

We must be able to have an editable photoshop version (PSD) of the document as well as a print ready PDF version incl any bleed necessary for A4 printing.

Target Market(s)

30-60YO Male and Female

Industry/Entity Type

Real Estate

Font styles to use
Sans Serif

Requirements
Must have
• Company Logo, contact details and copy provided

```html
<!DOCTYPE html>
<html lang="en">
<head>
<meta charset="utf-8">
<title>Harbourleaf Estates Agency – Referral Program Flyer and Banner</title>
<link rel="stylesheet" href="https://fonts.googleapis.com/css2?family=Roboto:wght@300;400;500;700;900&display=swap">
<style>
  :root {
    --stage: #d9d9d9;
    --black: #000000;
    --white: #ffffff;
    --teal: #1a7a8a;
    --teal-deep: #167485;
    --photo-light: #5fa8a6;
    --photo-mid: #3f8f8c;
    --photo-dark: #2b6f6b;
    --ink-teal: #1f7f8d;
  }
  * { box-sizing: border-box; margin: 0; padding: 0; }
  html, body { width: 1200px; height: 905px; overflow: hidden; }
  body {
    background: var(--stage);
    font-family: "Roboto", Arial, sans-serif;
    position: relative;
  }

  /* ---------- A4 flyer ---------- */
  .flyer {
    position: absolute;
    left: 46px; top: 68px;
    width: 540px; height: 764px;
    background: var(--white);
    box-shadow: 2px 3px 6px rgba(0,0,0,0.35);
    overflow: hidden;
  }
  .flyer-header {
    height: 164px;
    background: var(--black);
    display: flex; align-items: center; justify-content: center;
  }
  .brand-name {
    color: var(--white);
    font-weight: 500;
    letter-spacing: 0.5px;
    white-space: nowrap;
  }
  .flyer-header .brand-name { font-size: 38px; margin-top: 14px; }

  .hero {
    position: relative;
    height: 346px;
  }
  .hero-photo {
    position: absolute; inset: 0;
    background: linear-gradient(100deg, var(--photo-light) 0%, var(--photo-mid) 55%, var(--photo-dark) 100%);
  }
  .headline {
    position: absolute;
    left: 32px; top: 72px;
    color: var(--white);
    font-weight: 300;
    font-size: 32px;
    line-height: 42px;
  }
  .headline strong { font-weight: 700; }
  .headline .big { font-size: 36px; }

  .terms {
    height: 163px;
    padding: 44px 32px 0;
    color: var(--ink-teal);
    font-size: 14.4px;
    font-weight: 300;
    line-height: 22px;
    text-align: justify;
  }
  .terms strong { font-weight: 500; }

  .flyer-footer {
    height: 91px;
    background: var(--teal);
    color: var(--white);
    display: flex; align-items: center; justify-content: space-between;
    padding: 0 32px;
  }
  .contact-list { list-style: none; font-size: 14px; line-height: 23px; }
  .contact-list li { display: flex; align-items: center; gap: 4px; }
  .contact-list .web { font-weight: 500; }
  .icon { width: 19px; height: 19px; flex: none; }
  .phone { display: flex; align-items: center; gap: 6px; font-size: 23px; font-weight: 400; }
  .phone .icon { width: 20px; height: 20px; }

  /* ---------- Digital banner ---------- */
  .banner {
    position: absolute;
    left: 614px; top: 328px;
    width: 539px; height: 135px;
    display: flex;
    box-shadow: 2px 3px 6px rgba(0,0,0,0.35);
  }
  .banner-brand {
    width: 240px; background: var(--black);
    display: flex; align-items: center; justify-content: center;
  }
  .banner-brand .brand-name { font-size: 19px; }
  .banner-hero { position: relative; flex: 1; }
  .banner-hero .hero-photo { background: linear-gradient(100deg, var(--photo-light) 0%, var(--photo-mid) 60%, var(--photo-dark) 100%); }
  .banner-headline {
    position: absolute; left: 17px; top: 12px;
    color: var(--white);
    font-weight: 300; font-size: 17px; line-height: 23.5px;
  }
  .banner-headline strong { font-weight: 700; font-size: 19px; }
</style>
</head>
<body>

<article class="flyer">
  <header class="flyer-header">
    <span class="brand-name">HARBOURLEAF ESTATES</span>
  </header>

  <section class="hero">
    <div class="hero-photo" role="img" aria-label="Teal-tinted photo of a smiling man in shirt and tie pointing at the offer, with a house and garden behind"></div>
    <h1 class="headline">
      Invite your friends<br>
      and <strong>receive $250</strong><br>
      and <strong>they get</strong><br>
      <strong class="big">2 months free</strong><br>
      management! *
    </h1>
  </section>

  <p class="terms">
    <strong>*$250 referral fee paid</strong> when the owner you refer signs their property for Management with Harbourleaf Estates Agency. Your referral must be submitted prior to signing on our website using the referral form on this page: <strong>http://www.harbourleafestates.com.au/referral-program/</strong>
  </p>

  <footer class="flyer-footer">
    <ul class="contact-list">
      <li class="web">
        <svg class="icon" viewBox="0 0 20 20" aria-hidden="true">
          <circle cx="10" cy="10" r="9.5" fill="#fff"/>
          <g fill="none" stroke="#1a7a8a" stroke-width="1.1">
            <circle cx="10" cy="10" r="5.5"/>
            <ellipse cx="10" cy="10" rx="2.4" ry="5.5"/>
            <line x1="4.5" y1="10" x2="15.5" y2="10"/>
          </g>
        </svg>
        www.harbourleafestates.com.au
      </li>
      <li>
        <svg class="icon" viewBox="0 0 20 20" aria-hidden="true">
          <circle cx="10" cy="10" r="9.5" fill="#fff"/>
          <rect x="5" y="6.5" width="10" height="7" fill="none" stroke="#1a7a8a" stroke-width="1.2"/>
          <polyline points="5,6.5 10,10.5 15,6.5" fill="none" stroke="#1a7a8a" stroke-width="1.2"/>
        </svg>
        referrals@harbourleafestates.com.au
      </li>
    </ul>
    <div class="phone">
      <svg class="icon" viewBox="0 0 20 20" aria-hidden="true">
        <circle cx="10" cy="10" r="9.5" fill="#fff"/>
        <path d="M7 5.2c.5-.3 1-.2 1.3.3l.9 1.6c.2.4.1.9-.3 1.2l-.6.4c.5 1.2 1.3 2.1 2.4 2.7l.5-.6c.3-.4.8-.5 1.2-.2l1.5 1c.4.3.5.9.2 1.3l-.6.9c-.5.6-1.3.8-2 .5-2.6-1.1-4.4-3.1-5.2-5.8-.2-.7 0-1.5.7-1.9z" fill="#1a7a8a"/>
      </svg>
      0400 555 218
    </div>
  </footer>
</article>

<aside class="banner">
  <div class="banner-brand">
    <span class="brand-name">HARBOURLEAF ESTATES</span>
  </div>
  <div class="banner-hero">
    <div class="hero-photo" role="img" aria-label="Teal-tinted photo of a smiling man pointing at the offer in front of a house"></div>
    <p class="banner-headline">
      Invite your friends and<br>
      <strong>receive $250</strong><br>
      and <strong>they get</strong><br>
      <strong>2 months free</strong><br>
      management! *
    </p>
  </div>
</aside>

</body>
</html>
```